RIVERSTONE PAVING & EARTHWORKS

I would like the front of the card to have my logo centred.
I need it to have my contact details on the back of the card which are: RiverstonePavingEarthworks@mailbrook.net
0439268417
and a Facebook icon

```html
<!DOCTYPE html>
<html lang="en">
<head>
<meta charset="utf-8">
<title>Riverstone Paving &amp; Earthworks – Business Card</title>
<link href="https://fonts.googleapis.com/css2?family=Russo+One&family=Roboto:wght@400&display=swap" rel="stylesheet">
<style>
  :root {
    --page-bg: #1c1c1d;
    --card-bg: #141414;
    --brand-blue: #1d8ad6;
    --blue-light: #29b6e8;
    --blue-deep: #0a3f95;
    --silver: #b9b9b9;
    --contact-text: #e9f4fb;
  }
  * { margin: 0; padding: 0; box-sizing: border-box; }
  html, body {
    width: 1200px; height: 900px; overflow: hidden;
    background: var(--page-bg);
  }
  .stage {
    width: 1200px; height: 900px;
    display: flex; flex-direction: column;
    align-items: center; justify-content: center; gap: 50px;
  }
  .card {
    position: relative;
    width: 630px; height: 360px;
    background: var(--card-bg);
    border-radius: 16px;
    overflow: hidden;
    box-shadow: 0 14px 30px rgba(0,0,0,.55);
  }

  /* Front */
  .card--front {
    display: flex; flex-direction: column;
    align-items: center; justify-content: center; gap: 18px;
  }
  .brand-mark {
    width: 84px; height: 84px; border-radius: 50%;
    background: var(--brand-blue);
    flex: none;
  }
  .brand-name {
    font-family: "Russo One", sans-serif;
    font-weight: 400;
    color: var(--brand-blue);
    text-transform: uppercase;
    line-height: 1.08;
  }
  .brand-name span { display: block; }
  .card--front .brand-name { font-size: 32px; text-align: center; }

  /* Back */
  .card--back .brand-name {
    position: absolute; left: 70px; top: 44px;
    font-size: 30px;
  }
  .card--back .brand-name .brand-sub { padding-left: 26px; }

  .contact-band {
    position: absolute; left: 0; top: 198px;
    width: 420px; height: 64px;
  }
  .contact-band svg { position: absolute; inset: 0; }
  .contact-list {
    position: absolute; left: 34px; top: 10px;
    list-style: none;
    font-family: "Roboto", sans-serif; font-size: 14.5px;
    color: var(--contact-text); line-height: 22px;
  }
  .social-badge {
    position: absolute; left: 360px; top: 21px;
    width: 22px; height: 22px; border-radius: 4px;
    background: var(--contact-text);
  }
  .mark-large {
    position: absolute; right: 28px; top: 110px;
    width: 190px; height: 190px; border-radius: 50%;
    background: linear-gradient(160deg, var(--blue-light), var(--blue-deep));
  }
</style>
</head>
<body>
<main class="stage">

  <section class="card card--front" aria-label="Card front">
    <div class="brand-mark" aria-hidden="true"></div>
    <h1 class="brand-name">
      <span>Riverstone Paving</span>
      <span>&amp; Earthworks</span>
    </h1>
  </section>

  <section class="card card--back" aria-label="Card back">
    <h2 class="brand-name">
      <span>Riverstone Paving</span>
      <span class="brand-sub">&amp; Earthworks</span>
    </h2>

    <div class="contact-band">
      <svg viewBox="0 0 420 64" width="420" height="64" aria-hidden="true">
        <defs>
          <linearGradient id="bandBlue" x1="0" y1="0" x2="1" y2="0">
            <stop offset="0" stop-color="#29b6e8"/>
            <stop offset="1" stop-color="#0a3f95"/>
          </linearGradient>
        </defs>
        <polygon points="0,0 392,0 410,64 0,64" fill="#b9b9b9"/>
        <polygon points="0,5 390,5 406,59 0,59" fill="url(#bandBlue)"/>
      </svg>
      <ul class="contact-list">
        <li>P : 0439268417</li>
        <li>E : RiverstonePavingEarthworks@mailbrook.net</li>
      </ul>
      <span class="social-badge" role="img" aria-label="Social media page"></span>
    </div>

    <div class="mark-large" aria-hidden="true"></div>
  </section>

</main>
</body>
</html>
```